Designs of screens for job search mobile app

Design the following screens:

1. Login
2. Job search results in tabs
3. Job details in cards format
4. Profile
5. Settings

Logo and references are provided. The app need to be playful, easy to use, different from traditional job search app like Workvane, ProLattice and others and targeted to Millennial users (age 18-30).

The main app reference is Piqto, in terms of the colorful and fun color and font scheme.

Target Market(s)

Millennial users (age 18-30).

Requirements
Must have
• A fun, playful feel

```html
<!DOCTYPE html>
<html lang="en">
<head>
<meta charset="utf-8">
<title>RoamWork – job search app screens</title>
<link href="https://fonts.googleapis.com/css2?family=Lato:wght@400;700&display=swap" rel="stylesheet">
<style>
:root{
  --cyan:#3fd0f6;
  --cyan-deep:#22b8e6;
  --pink:#f0457a;
  --pink-soft:#f2688f;
  --blue-top:#3fa3f2;
  --blue-bottom:#3a78ef;
  --orange:#ff6a3d;
  --ink:#333;
  --muted:#9a9a9a;
  --line:#e6e6e6;
  --panel:#f2f2f2;
  --green:#3cc36a;
}
*{box-sizing:border-box;margin:0;padding:0}
html,body{width:1200px;height:1200px;overflow:hidden;background:#fff}
body{font-family:'Lato',sans-serif;color:var(--ink);position:relative}
.screen{position:absolute;width:226px;height:404px;overflow:hidden;background:#fff}
.a{position:absolute}
.status{position:absolute;left:0;top:0;width:100%;height:12px;font-size:6px;color:#fff;display:flex;justify-content:space-between;align-items:center;padding:0 4px}
.status b{font-weight:700}
.appbar{position:absolute;left:0;top:12px;width:100%;height:28px;display:flex;align-items:center;justify-content:center;color:#fff;font-size:10px;letter-spacing:.3px;background:var(--cyan)}
.menu{position:absolute;left:10px;top:10px;width:10px;height:8px;border-top:1.3px solid #fff;border-bottom:1.3px solid #fff}
.menu::after{content:"";position:absolute;left:0;top:2.2px;width:10px;border-top:1.3px solid #fff}
.splash{background:var(--cyan)}
.brand{position:absolute;left:0;top:186px;width:100%;display:flex;align-items:center;justify-content:center;gap:7px;color:#fff;font-size:26px}
.brand i{width:24px;height:24px;border-radius:50%;background:#fff;display:block}
.onboard{background:var(--cyan)}
.onboard h2{position:absolute;top:218px;width:100%;text-align:center;color:#fff;font-size:15px;font-weight:400}
.onboard p{position:absolute;top:242px;left:28px;width:170px;text-align:center;color:#fff;font-size:7px;line-height:9.5px}
.dots{position:absolute;top:309px;left:96px;display:flex;gap:4px}
.dots span{width:5px;height:5px;border-radius:50%;background:#fff}
.dots span:first-child{background:#1a9cc0}
.field{position:absolute;left:15px;width:198px;border-bottom:1px solid var(--line);height:32px}
.field .lbl{font-size:7.5px;color:#333}
.field .val{font-size:6.5px;color:var(--muted);margin-top:4px}
.field svg{position:absolute;right:4px;top:10px}
.link{position:absolute;top:198px;width:100%;text-align:center;font-size:7.5px;color:var(--cyan-deep);text-decoration:underline}
.btn{position:absolute;top:419px;height:30px;border-radius:15px;font-size:7.5px;display:flex;align-items:center;justify-content:center}
.job{position:absolute;left:0;width:226px;height:50px;border-bottom:1px solid var(--line)}
.job .logo{position:absolute;left:10px;top:9px;width:30px;height:30px;border-radius:50%;background:#e9eef2}
.job .t{position:absolute;left:49px;top:4px;font-size:8.5px;color:#333;white-space:nowrap}
.job .c{position:absolute;left:49px;top:16px;font-size:6px;color:#bbb}
.job .s{position:absolute;left:49px;top:25px;font-size:6.5px;color:#666}
.job .time{position:absolute;right:8px;bottom:3px;font-size:6px;color:#bbb}
.swipe{position:absolute;left:0;top:0;width:72px;height:50px;background:var(--pink);display:flex;align-items:center;justify-content:space-around}
.profile-head{position:absolute;left:0;top:0;width:100%;height:130px;background:linear-gradient(180deg,#ee3f74,#f05a87)}
.avatar{position:absolute;width:33px;height:35px;left:97px;top:14px;background:#d9c9bd;border:2px solid #fff}
.pname{position:absolute;width:100%;text-align:center;color:#fff;font-size:8.5px;letter-spacing:.3px}
.psub{position:absolute;width:100%;text-align:center;color:#fbd0dd;font-size:6.5px;line-height:8.5px}
.pbio{position:absolute;width:100%;text-align:center;color:#fde3ea;font-size:7px;line-height:9px;padding:0 30px}
.rating{position:absolute;right:12px;top:22px;font-size:6.5px;color:#fbd0dd}
.tabs{position:absolute;left:0;top:112px;width:100%;height:18px;display:flex;justify-content:space-around;align-items:center;color:#fff;font-size:6.5px;font-weight:700}
.tabline{position:absolute;top:127px;height:3px;width:78px;background:var(--cyan)}
.card{position:absolute;left:8px;width:212px;background:#fff;box-shadow:0 1px 2px rgba(0,0,0,.08)}
.card h4{font-size:6.5px;font-weight:700;color:#444;padding:8px 8px 6px;border-bottom:1px solid var(--line)}
.plus{position:absolute;right:10px;top:4px;color:var(--pink);font-size:10px}
.mini{font-size:5.2px;color:#999;line-height:7px}
.pf{position:absolute;left:16px;width:194px;border-bottom:1px solid var(--line);height:30px}
.pf .lbl{font-size:6.5px;color:#999}
.pf .val{font-size:7.5px;color:#333;margin-top:5px}
.shot{position:absolute}
.details{background:linear-gradient(180deg,var(--blue-top),var(--blue-bottom))}
.details .appbar{background:transparent}
.round{position:absolute;top:346px;width:36px;height:36px;border-radius:50%;background:#fff;display:flex;align-items:center;justify-content:center;box-shadow:0 2px 4px rgba(0,0,0,.15)}
.chip{display:inline-block;font-size:5.5px;color:#fff;background:#bdbdbd;border-radius:6px;padding:1.5px 9px;margin-right:3px}
.settings{background:#f1f1f1}
.srow{position:absolute;left:20px;width:190px;font-size:7.5px;color:#333;height:24px;border-bottom:1px solid #eee;display:flex;align-items:center;justify-content:space-between}
.srow:last-child{border-bottom:0}
.dot{width:14px;height:14px;border-radius:50%;background:#3a86d8;display:block}
.toggle{width:28px;height:9px;border-radius:5px;background:#dfe8ee;position:relative}
.toggle i{position:absolute;top:-2px;width:13px;height:13px;border-radius:50%}
.logout{position:absolute;left:0;top:368px;width:100%;height:36px;background:var(--orange);color:#fff;font-size:12px;display:flex;align-items:center;justify-content:center}
</style>
</head>
<body>

<!-- Splash -->
<section class="screen splash" style="left:136px;top:189px">
  <div class="status"><span>●●●○○ ORBIT</span><b>4:21 PM</b><span>22% ▭</span></div>
  <div class="brand"><i></i><span>RoamWork</span></div>
</section>

<!-- Onboarding -->
<section class="screen onboard" style="left:373px;top:189px">
  <div class="status"><span>●●●○○ ORBIT</span><b>4:21 PM</b><span>22% ▭</span></div>
  <div class="a" role="img" aria-label="Illustration of a work bag with a map pin among clouds" style="left:50px;top:64px;width:126px;height:126px;border-radius:50%;background:#1c9596"></div>
  <h2>Search Easily Nearby</h2>
  <p>Find roles close to home in a tap. Browse fresh openings around you, save the ones you love and apply straight from your phone, any time, anywhere.</p>
  <div class="dots"><span></span><span></span><span></span><span></span></div>
  <div class="a" style="left:177px;top:359px;width:36px;height:36px;border-radius:50%;background:var(--pink);display:flex;align-items:center;justify-content:center">
    <svg width="14" height="12" viewBox="0 0 14 12"><path d="M1 6h12M8 1l5 5-5 5" stroke="#fff" stroke-width="1.4" fill="none"/></svg>
  </div>
</section>

<!-- Search job -->
<section class="screen" style="left:608px;top:189px">
  <div class="status" style="background:var(--cyan)"><span>●●●○○ ORBIT</span><b>4:21 PM</b><span>22% ▭</span></div>
  <div class="appbar"><span class="menu"></span>SEARCH JOB</div>
  <div class="field" style="top:59px"><div class="lbl">Job Title, Keyword, Company</div><div class="val">Mobile</div><svg width="8" height="6"><path d="M1 3l2 2 4-4" stroke="var(--green)" fill="none"/></svg></div>
  <div class="field" style="top:103px"><div class="lbl">Country</div><div class="val">Singapore</div><svg width="8" height="6"><path d="M1 3l2 2 4-4" stroke="var(--green)" fill="none"/></svg></div>
  <div class="field" style="top:143px"><div class="lbl">Location</div><div class="val">Singapore</div><svg width="14" height="14" style="top:6px"><circle cx="7" cy="7" r="5" stroke="var(--pink)" fill="none" stroke-width="1.2"/><circle cx="7" cy="7" r="2.2" fill="var(--pink)"/><path d="M7 0v2M7 12v2M0 7h2M12 7h2" stroke="var(--pink)"/></svg></div>
  <div class="link">Show Advance Search</div>
  <div class="btn" style="top:230px;left:14px;width:94px;background:var(--pink);color:#fff">SEARCH</div>
  <div class="btn" style="top:230px;left:118px;width:94px;border:1px solid #555;color:#333">CANCEL</div>
</section>

<!-- Search results -->
<section class="screen" style="left:840px;top:189px">
  <div class="status" style="background:var(--cyan)"><span>●●●○○ ORBIT</span><b>4:21 PM</b><span>22% ▭</span></div>
  <div class="appbar">
    <svg class="a" style="left:10px;top:9px" width="7" height="11"><path d="M6 1L1 5.5 6 10" stroke="#fff" fill="none" stroke-width="1.3"/></svg>
    SEARCH RESULTS
    <svg class="a" style="right:10px;top:8px" width="12" height="12"><path d="M1 1h10L7 6v5L5 10V6z" stroke="#fff" fill="none"/></svg>
  </div>
  <div class="job" style="top:47px"><span class="logo"></span><span class="t">Mobile Developer Require</span><span class="c">Voltwise, Singapore</span><span class="s">$80k - $90k per annum</span><span class="time">Now</span></div>
  <div class="job" style="top:97px"><span class="logo"></span><span class="t">System Architect</span><span class="c">Nimbra, Singapore</span><span class="s">$80k - $90k per annum</span><span class="time">4 min</span></div>
  <div class="job" style="top:146px"><span class="logo"></span><span class="t">Mobile Part time Developer</span><span class="c">Emberline, Singapore</span><span class="s">$60k - $70k per annum</span><span class="time">1 hrs</span></div>
  <div class="job" style="top:196px"><span class="logo"></span><span class="t">BACKEND Developer</span><span class="c">Parcelo, Singapore</span><span class="s">$100k - $120k per annum</span><span class="time">2 hrs</span></div>
  <div class="job" style="top:243px"><span class="logo"></span><span class="t">Mobile Developer Opening</span><span class="c">Skarva, Singapore</span><span class="s">$180k - $190k per annum</span><span class="time">Now</span></div>
  <div class="job" style="top:293px;border-bottom:0">
    <div class="swipe">
      <svg width="14" height="14"><rect x="1" y="1" width="12" height="12" rx="1.5" stroke="#fff" fill="none"/><rect x="4" y="1" width="6" height="4" stroke="#fff" fill="none"/></svg>
      <svg width="15" height="11"><rect x="1" y="1" width="13" height="9" stroke="#fff" fill="none"/><path d="M1 1l6.5 5L14 1" stroke="#fff" fill="none"/></svg>
    </div>
    <span class="logo" style="left:80px"></span><span class="t" style="left:120px">Mobile Developer for Brickly</span><span class="c" style="left:120px">Brickly, Singapore</span><span class="s" style="left:120px">$80k - $90k per annum</span>
  </div>
  <div class="job" style="top:343px;border-top:1px solid var(--line)"><span class="logo"></span><span class="t">Mobile Freelancer Work</span><span class="c">Covaro, Singapore</span><span class="s">$20k - $22k per annum</span><span class="time">1 hrs</span></div>
  <div class="job" style="top:393px"><span class="logo"></span><span class="t">BACKEND Developer</span></div>
</section>

<!-- Profile: about me -->
<section class="screen" style="left:16px;top:608px;background:var(--panel)">
  <div class="profile-head"></div>
  <div class="status"><span>●●●○○ ORBIT</span><b>4:21 PM</b><span>22% ▭</span></div>
  <span class="menu" style="top:26px"></span>
  <span class="rating">4.2/5 <span style="color:#ffd23f">★</span></span>
  <div class="avatar" role="img" aria-label="Profile photo of the user"></div>
  <div class="pname" style="top:58px">LEO MARSH</div>
  <div class="psub" style="top:69px">Singapore<br>leomarsh@mailbox.test</div>
  <div class="pbio" style="top:89px">Short bio about the member goes here in a couple of friendly lines.</div>
  <div class="tabs"><span>ABOUT ME</span><span>PORTFOLIO</span><span>PROFILE</span></div>
  <div class="tabline" style="left:0"></div>
  <div class="card" style="top:142px;height:72px"><h4>Summary</h4>
    <p class="mini" style="padding:6px 8px">Motivated mobile developer who loves clean code, quick prototypes and friendly teams. Five years shipping apps used by thousands of people, now looking for a playful studio with room to learn and lead new features.</p></div>
  <div class="card" style="top:224px;height:64px"><h4>Work Experience</h4><span class="plus">+</span>
    <span class="a" style="left:9px;top:27px;width:22px;height:22px;border-radius:50%;background:#d7e8f4"></span>
    <div class="a" style="left:50px;top:29px;font-size:5.8px;font-weight:700;color:#333">QUILLON SOFTWARE PVT.LTD</div>
    <div class="a mini" style="left:50px;top:36px">Mobile Developer<br>September 15 - Present</div></div>
  <div class="card" style="top:298px;height:64px"><h4>Education</h4><span class="plus">+</span>
    <span class="a" style="left:9px;top:27px;width:22px;height:22px;background:#e4e4e4"></span>
    <div class="a" style="left:50px;top:29px;font-size:5.8px;font-weight:700;color:#333">R.M College of Engineering</div>
    <div class="a mini" style="left:50px;top:36px">Westbrook University<br>September 10 - March 14</div></div>
  <div class="card" style="top:372px;height:40px"><h4>Skills</h4><span class="plus">+</span>
    <div style="padding:4px 8px"><span class="chip">Mobile</span><span class="chip">Backend</span><span class="chip">UI Design</span><span class="chip">Testing</span></div></div>
</section>

<!-- Profile: personal details -->
<section class="screen" style="left:254px;top:608px">
  <div class="profile-head"></div>
  <div class="status"><span>●●●○○ ORBIT</span><b>4:21 PM</b><span>22% ▭</span></div>
  <span class="menu" style="top:26px"></span>
  <span class="rating" style="top:18px">4.2/5 <span style="color:#ffd23f">★</span></span>
  <div class="avatar" role="img" aria-label="Profile photo of the user" style="top:10px"></div>
  <div class="pname" style="top:51px">LEO MARSH</div>
  <div class="psub" style="top:62px">Singapore<br>leomarsh@mailbox.test</div>
  <div class="pbio" style="top:82px">Short bio about the member goes here in a couple of friendly lines.</div>
  <div class="tabs"><span>ABOUT ME</span><span>PORTFOLIO</span><span>PROFILE</span></div>
  <div class="tabline" style="left:148px"></div>
  <div class="a" style="right:16px;top:140px;font-size:7.5px;color:var(--cyan-deep);font-weight:700">Edit</div>
  <div class="pf" style="top:154px"><div class="lbl">First Name</div><div class="val">LEO</div></div>
  <div class="pf" style="top:191px"><div class="lbl">Last Name</div><div class="val">MARSH</div></div>
  <div class="pf" style="top:228px"><div class="lbl">Email</div><div class="val">leomarsh@mailbox.test</div></div>
  <div class="pf" style="top:265px"><div class="lbl">Date of Birth</div><div class="val">25 July 1985</div></div>
  <div class="pf" style="top:302px"><div class="lbl">Gender</div><div class="val">Male</div></div>
  <div class="pf" style="top:339px"><div class="lbl">City</div><div class="val">Singapore</div></div>
  <div class="pf" style="top:376px"><div class="lbl">Country</div><div class="val">Singapore</div></div>
</section>

<!-- Profile: portfolio -->
<section class="screen" style="left:488px;top:608px">
  <div class="profile-head"></div>
  <div class="status"><span>●●●○○ ORBIT</span><b>4:21 PM</b><span>22% ▭</span></div>
  <span class="menu" style="top:26px"></span>
  <span class="rating" style="top:18px">4.2/5 <span style="color:#ffd23f">★</span></span>
  <div class="avatar" role="img" aria-label="Profile photo of the user" style="top:10px"></div>
  <div class="pname" style="top:51px">LEO MARSH</div>
  <div class="psub" style="top:62px">Singapore<br>leomarsh@mailbox.test</div>
  <div class="pbio" style="top:82px">Short bio about the member goes here in a couple of friendly lines.</div>
  <div class="tabs"><span>ABOUT ME</span><span>PORTFOLIO</span><span>PROFILE</span></div>
  <div class="tabline" style="left:74px"></div>
  <div class="shot" role="img" aria-label="Portfolio photo of an app on a phone" style="left:6px;top:140px;width:74px;height:70px;background:linear-gradient(135deg,#4a5560,#2b3038)"></div>
  <div class="shot" role="img" aria-label="Portfolio photo of a game on a tablet" style="left:86px;top:140px;width:133px;height:70px;background:linear-gradient(135deg,#6a6f78,#c9883a)"></div>
  <div class="shot" role="img" aria-label="Portfolio photo of a hand holding a phone" style="left:6px;top:218px;width:66px;height:69px;background:linear-gradient(135deg,#5f8a3a,#2e4a20)"></div>
  <div class="shot" role="img" aria-label="Portfolio screenshot of a reading app" style="left:78px;top:218px;width:68px;height:69px;background:linear-gradient(135deg,#1f4b55,#163239)"></div>
  <div class="shot" role="img" aria-label="Portfolio photo of a phone app in hand" style="left:152px;top:218px;width:67px;height:69px;background:linear-gradient(135deg,#4b4f55,#2a2d31)"></div>
  <div class="shot" role="img" aria-label="Portfolio mock-up of three phones" style="left:6px;top:294px;width:112px;height:69px;background:linear-gradient(135deg,#3f5e6e,#22343c)"></div>
  <div class="shot" role="img" aria-label="Portfolio photo of a map app on a desk" style="left:125px;top:294px;width:94px;height:69px;background:linear-gradient(135deg,#d8d1c6,#9e968a)"></div>
  <div class="shot" role="img" aria-label="Portfolio photo of devices" style="left:6px;top:370px;width:213px;height:40px;background:linear-gradient(135deg,#3e4247,#777d84)"></div>
</section>

<!-- Job details card -->
<section class="screen details" style="left:721px;top:608px">
  <div class="status"><span>●●●○○ ORBIT</span><b>4:21 PM</b><span>22% ▭</span></div>
  <div class="appbar"><span class="menu"></span>JOB DETAILS</div>
  <div class="a" style="left:22px;top:73px;width:184px;height:260px;background:#fff;box-shadow:0 3px 0 -1px #e9eef6,0 6px 0 -2px #dfe6f1">
    <div class="a" style="top:32px;width:100%;text-align:center;font-size:12px;color:#333">Ravenmoor</div>
    <div class="a" style="top:47px;width:100%;text-align:center;font-size:6px;color:#555">Singapore and USA</div>
    <div class="a" style="top:57px;left:0;width:100%;border-top:1px solid var(--line)"></div>
    <div class="a" style="left:8px;top:65px;font-size:8.5px;color:#222">SYSTEM ARCHITECH</div>
    <div class="a" style="right:8px;top:66px;font-size:5.5px;color:#333">2 hrs</div>
    <div class="a" style="left:8px;top:76px;font-size:5.5px;color:#333">100k - 200k per annum</div>
    <p class="a" style="left:8px;top:86px;width:168px;font-size:6.8px;line-height:7.6px;color:#555;text-align:justify">Design and own the architecture of our mobile and web platform. Work with product, design and engineering to plan scalable services, review code, mentor developers and keep our systems fast, safe and simple. You will shape the stack, lead technical decisions and help the team grow with clear guidelines every day.</p>
    <div class="a" style="left:8px;top:162px;font-size:6.5px;color:var(--pink)">Friends Working / Worked</div>
    <div class="a" role="img" aria-label="Friend photo" style="left:12px;top:173px;width:22px;height:22px;border-radius:50%;background:#d8c2b0"></div>
    <div class="a" role="img" aria-label="Friend photo" style="left:56px;top:173px;width:22px;height:22px;border-radius:50%;background:#c9ad96"></div>
    <div class="a" role="img" aria-label="Friend photo" style="left:104px;top:173px;width:22px;height:22px;border-radius:50%;background:#e6cfb1"></div>
    <div class="a" style="left:15px;top:198px;font-size:6px">Ivo</div>
    <div class="a" style="left:54px;top:198px;font-size:6px">Noah.p</div>
    <div class="a" style="left:106px;top:198px;font-size:6px">Mira</div>
    <div class="a" style="left:8px;top:213px;font-size:6px">Skils</div>
    <div class="a" style="left:12px;top:226px"><span class="chip">Mobile</span><span class="chip">Backend</span><span class="chip">Mobile Studio</span></div>
  </div>
  <div class="a" style="left:84px;top:52px;width:58px;height:58px;border-radius:50%;background:#f1f1f1;box-shadow:0 1px 3px rgba(0,0,0,.15)"></div>
  <div class="round" style="left:19px"><svg width="14" height="14"><path d="M2 2l10 10M12 2L2 12" stroke="var(--orange)" stroke-width="1.8"/></svg></div>
  <div class="round" style="left:93px;width:42px;height:42px;top:343px"><svg width="16" height="10"><path d="M1 1l7 7 7-7" stroke="#3a78ef" stroke-width="1.8" fill="none"/></svg></div>
  <div class="round" style="left:164px"><svg width="16" height="12"><path d="M1 6l5 5L15 1" stroke="var(--green)" stroke-width="2" fill="none"/></svg></div>
</section>

<!-- Settings -->
<section class="screen settings" style="left:958px;top:608px">
  <div class="status" style="background:var(--cyan)"><span>●●●○○ ORBIT</span><b>4:21 PM</b><span>22% ▭</span></div>
  <div class="appbar"><span class="menu"></span>SETTINGS</div>
  <div class="a" style="left:8px;top:53px;width:210px;height:72px;background:#fff">
    <div style="font-size:6.5px;font-weight:700;padding:7px 8px;border-bottom:1px solid #eee">Notification</div>
  </div>
  <div class="srow" style="top:82px;left:20px;border-bottom:0">Job Message<span class="toggle"><i style="right:-2px;background:var(--cyan)"></i></span></div>
  <div class="srow" style="top:102px;border-bottom:0">Send Notification via email<span class="toggle"><i style="left:-2px;background:#555"></i></span></div>
  <div class="a" style="left:8px;top:136px;width:210px;height:108px;background:#fff"></div>
  <div class="srow" style="top:138px">Like us on Friendlane<span class="dot"></span></div>
  <div class="srow" style="top:167px">Like us on ProLattice<span class="dot"></span></div>
  <div class="srow" style="top:194px">Like us on ProLattice<span class="dot" style="background:#2aa3e8"></span></div>
  <div class="srow" style="top:222px;border-bottom:0">Rate us on application store<span style="display:flex;gap:8px"><span class="dot" style="background:#ccc"></span><span class="dot" style="background:#ccc"></span></span></div>
  <div class="a" style="left:8px;top:258px;width:210px;height:91px;background:#fff"></div>
  <div class="srow" style="top:261px">Help</div>
  <div class="srow" style="top:290px">Privacy Policy</div>
  <div class="srow" style="top:321px;border-bottom:0">Terms of Use</div>
  <div class="logout">LOGOUT</div>
</section>

</body>
</html>
```